Wedding Day Custom Wine Label - Tasmanian (Tamar Valley) wine

I am looking for a custom design that will be put on a wine label to commemorate a very good friend's wedding day.

We will need to be able to take the design and print it on to sticker labels that we can put on to wine bottles.

The bride and groom have asked for a simplistic label design (see example image attached). We need two labels. One for "Pinot Noir" wine and the other for "Chardonnay" wine. We would like the label to say:

The Hartwell's
Pinot Noir
2023
Tamar Valley

and for for the other wine variety:

The Hartwell's
Chardonnay
2023
Tamar Valley

smaller text below to say:

13.5% ALC/VOL 750ML
MEGAN & LIAM - 31.10.2024

I am happy to consider other variations - the bride & groom would prefer something minimalistic. Elegant and classy.

Target Market(s)

the bride & groom

Requirements
Must have
• Wedding date (31.10.2024). Wine type (Pinot Noir or Chardonnay).
Should not have
• images not essential

```html
<!DOCTYPE html>
<html lang="en">
<head>
<meta charset="utf-8">
<title>The Hartwell's – Wedding Wine Labels</title>
<link rel="stylesheet" href="https://fonts.googleapis.com/css2?family=Josefin+Sans:wght@400;600;700&family=Great+Vibes&display=swap">
<style>
  :root {
    --ink: #000000;
    --paper: #ffffff;
  }
  html, body {
    margin: 0;
    padding: 0;
    width: 776px;
    height: 1200px;
    overflow: hidden;
    background: var(--paper);
  }
  .label-sheet { display: block; width: 776px; height: 1200px; }
  .frame-outer { fill: var(--paper); stroke: var(--ink); stroke-width: 13; }
  .frame-inner { fill: none; stroke: var(--ink); stroke-width: 2.5; }
  .frame-halo { fill: var(--paper); stroke: var(--paper); stroke-width: 32; stroke-linejoin: round; }
  .rule { stroke: var(--ink); stroke-width: 1.5; }
  .name-knockout { fill: var(--paper); }
  .script-the { font-family: "Great Vibes", cursive; font-size: 44px; fill: var(--ink); }
  .family-name { font-family: "Josefin Sans", sans-serif; font-weight: 700; font-size: 80px; fill: var(--ink); }
  .couple-date { font-family: "Josefin Sans", sans-serif; font-weight: 600; font-size: 20px; fill: var(--ink); }
  .variety-pill { fill: var(--ink); }
  .variety-name { font-family: "Josefin Sans", sans-serif; font-weight: 600; font-size: 33px; fill: var(--paper); }
  .vintage { font-family: "Josefin Sans", sans-serif; font-weight: 700; font-size: 32px; fill: var(--ink); }
  .region { font-family: "Josefin Sans", sans-serif; font-weight: 400; font-size: 17px; letter-spacing: 2px; fill: var(--ink); }
  .volume { font-family: "Josefin Sans", sans-serif; font-weight: 700; font-size: 9px; fill: var(--ink); }
  .dark-panel { fill: var(--ink); }
</style>
</head>
<body>
<svg class="label-sheet" viewBox="0 0 776 1200" xmlns="http://www.w3.org/2000/svg">
  <defs>
    <path id="badge-shape" d="M427,138 L598,189 Q610,193 610,205 L610,448 Q610,461 598,465 L439,512 Q427,516 415,512 L260,465 Q248,461 248,448 L248,205 Q248,193 260,189 Z"/>
    <path id="badge-inner" d="M427,158 L588,205 Q594,207 594,214 L594,440 Q594,447 588,449 L434,494 Q427,496 420,494 L270,449 Q264,447 264,440 L264,214 Q264,207 270,205 Z"/>
    <g id="badge-frame">
      <use href="#badge-shape" class="frame-outer"/>
      <use href="#badge-inner" class="frame-inner"/>
      <line class="rule" x1="300" y1="211" x2="384" y2="211"/>
      <line class="rule" x1="468" y1="211" x2="552" y2="211"/>
      <text class="script-the" x="427" y="222" text-anchor="middle">the</text>
      <rect class="name-knockout" x="212" y="232" width="432" height="78"/>
      <text class="family-name" x="428" y="305" text-anchor="middle" textLength="426" lengthAdjust="spacingAndGlyphs">HARTWELL'S</text>
      <text class="couple-date" x="427" y="332" text-anchor="middle">MEGAN &amp; LIAM ·31·10·2024</text>
      <rect class="variety-pill" x="287" y="341" width="280" height="42" rx="21"/>
      <text class="vintage" x="427" y="421" text-anchor="middle">2023</text>
      <line class="rule" x1="327" y1="428" x2="527" y2="428"/>
      <text class="region" x="427" y="447" text-anchor="middle">TAMAR VALLEY</text>
      <line class="rule" x1="327" y1="454" x2="527" y2="454"/>
      <text class="volume" x="427" y="468" text-anchor="middle">13.5% ALC/VOL • 750ML</text>
    </g>
  </defs>

  <g class="label label-pinot">
    <use href="#badge-frame"/>
    <text class="variety-name" x="427" y="374" text-anchor="middle">PINOT NOIR</text>
  </g>

  <g class="label label-chardonnay">
    <rect class="dark-panel" x="167" y="600" width="511" height="468"/>
    <g transform="translate(0,497)">
      <use href="#badge-shape" class="frame-halo"/>
      <rect class="name-knockout" x="204" y="226" width="448" height="90" rx="6"/>
      <use href="#badge-frame"/>
      <text class="variety-name" x="427" y="374" text-anchor="middle">CHARDONNAY</text>
    </g>
  </g>
</svg>
</body>
</html>
```